Tessel Vodka bottle label for grassroots distiller, micro-distiller in Kansas. Quillan Forge Distilli

We are located in South Central Kansas. Needing a design for a vodka label. The vodka will be distilled using white milo, which has not been done in the US as far as we know. We are in Kansas and a true "grass roots" business. We are starting on a shoestring, using bare essentials, and locally sourced components. We are looking for a clean, eye catching, grass roots feel. We also will be able to label it non gmo and Gluten free.

Target Market(s)

Upper mid-range price point. Target audience is professionals 25-50 with discretionary income and descerning taste.

Logo Text

Tessel Vodka, Sorghum Based Vodka. Non GMO, AND GLUTEN FREE. Quillan Forge Distilling, 847 W. 3rd Avenue, Kinsley, Ks.

Other font styles liked:
• Georgia, does not have to be, open

Colors
000000

Requirements
Must have
• Simple. Clean. And comply with PQX regulations for labeling found at www.PQX-regs.example
Nice to have
• Stylized image of White Milo. Proundly made in South Central Kansas with locally sourced grain.
Should not have
• Too many words. Exclusively Kansas.

```html
<!DOCTYPE html>
<html lang="en">
<head>
<meta charset="utf-8">
<title>Tessel Vodka — Label</title>
<link rel="stylesheet" href="https://fonts.googleapis.com/css2?family=Special+Elite&display=swap">
<style>
  :root {
    --label-ground: #1c1e21;
    --label-ground-deep: #141618;
    --ink-light: #f4f4f2;
    --wash-white: #ffffff;
    --wash-lavender: #aeb4ec;
    --wash-teal: #2bb3b1;
    --wash-mint: #bfe9e2;
  }
  html, body {
    margin: 0;
    padding: 0;
    overflow: hidden;
    background: var(--label-ground);
  }
  .label {
    position: relative;
    width: 1200px;
    height: 680px;
    overflow: hidden;
    background:
      radial-gradient(ellipse at 78% 40%, var(--label-ground-deep) 0%, transparent 45%),
      radial-gradient(ellipse at 22% 70%, var(--label-ground-deep) 0%, transparent 40%),
      var(--label-ground);
    font-family: "Special Elite", "Courier New", monospace;
    color: var(--ink-light);
  }
  .brand-name {
    position: absolute;
    top: 76px;
    left: 0;
    width: 100%;
    margin: 0;
    text-align: center;
    font-weight: 400;
    font-size: 34px;
    letter-spacing: 4px;
    font-variant: small-caps;
    line-height: 1;
  }
  .brand-name .initial { font-size: 46px; }
  .brand-name .word-gap { display: inline-block; width: 26px; }
  .emblem {
    position: absolute;
    left: 387px;
    top: 157px;
    width: 436px;
    height: 378px;
  }
  .origin {
    position: absolute;
    top: 550px;
    left: 0;
    width: 100%;
    margin: 0;
    text-align: center;
    font-size: 22px;
    letter-spacing: 3px;
    font-variant: small-caps;
    line-height: 1;
  }
  .origin .initial { font-size: 28px; }
  .claim {
    position: absolute;
    top: 176px;
    margin: 0;
    writing-mode: vertical-lr;
    text-orientation: upright;
    font-size: 10px;
    letter-spacing: 5.2px;
    line-height: 1;
    text-transform: uppercase;
  }
  .claim .initial { font-size: 14px; }
  .claim--left { left: 23px; }
  .claim--right { right: 17px; }
</style>
</head>
<body>
  <main class="label">
    <h1 class="brand-name"><span class="initial">T</span>essel<span class="word-gap"></span><span class="initial">V</span>odka</h1>

    <svg class="emblem" viewBox="0 0 436 378" role="img" aria-label="Watercolour wash in lavender and teal with a stylised white milo sorghum stalk">
      <defs>
        <radialGradient id="wash" cx="0.5" cy="0.4" r="0.6">
          <stop offset="0" stop-color="var(--wash-teal)"/>
          <stop offset="0.35" stop-color="var(--wash-mint)"/>
          <stop offset="0.7" stop-color="var(--wash-lavender)"/>
          <stop offset="1" stop-color="var(--wash-white)"/>
        </radialGradient>
      </defs>
      <polygon points="0,0 436,0 218,378" fill="url(#wash)"/>
    </svg>

    <p class="origin"><span class="initial">K</span>ansas</p>

    <p class="claim claim--left">Non gmo and <span class="initial">G</span>luten free</p>
    <p class="claim claim--right">Non gmo and <span class="initial">G</span>luten free</p>
  </main>
</body>
</html>
```